Roofing Company Modern look

I want a modern and sophisticated look for our roofing business.

Our address is :

4276 Pellman Crossing Rd
Orlando, Fl 32825

(407)-583-2716

www.SummitcrestShinglesFl.com

I also want to make sure on the back there is a spot to put
Project Manager Name :

Number:

Because the cards will be used by all sales people

Project Manager Name :

Also there are accreditation we have logos are uploaded here as well that I would like maybe on the back of card as well

I also want to highlight our special attributions or trades:

Residential & Commercial
Fully Insured
License # CCC4872196
Insurance Claims
Serving Central Florida Since 1992
Free Estimates

Contact Information for Business Card

Our address is :

4276 Pellman Crossing Rd
Orlando, Fl 32825

(407)-583-2716

Project Manager Name :

Residential & Commercial
Fully Insured
License # CCC4872196
Insurance Claims
Free Estimates

Font styles to use
Serif
Sans Serif

Colors
3176b5

Requirements
Must have
• Must have royal blue like my logo grey and black are the colors I like

```html
<!DOCTYPE html>
<html lang="en">
<head>
<meta charset="utf-8">
<title>Summitcrest Roofing &amp; Gutters – Business Card</title>
<link href="https://fonts.googleapis.com/css2?family=Open+Sans:wght@400;600;700&display=swap" rel="stylesheet">
<style>
  :root{
    --backdrop:#e4e4e4;
    --royal:#2a5ca8;
    --royal-light:#3176b5;
    --card-white:#f4f4f4;
    --ink:#4a4a4a;
    --charcoal:#4b4b4d;
    --white:#ffffff;
  }
  *{margin:0;padding:0;box-sizing:border-box}
  html,body{width:1200px;height:960px;overflow:hidden}
  body{background:var(--backdrop);font-family:"Open Sans",sans-serif;position:relative}

  .card{position:absolute;left:305px;width:592px;height:338px;overflow:hidden}
  .card--front{top:127px;background:var(--royal);color:var(--white)}
  .card--back{top:518px;background:var(--card-white);color:var(--ink)}

  .state-map{position:absolute;left:470px;top:0;width:380px;height:338px;
    background:radial-gradient(ellipse 60% 70% at 60% 45%,rgba(49,118,181,.55),rgba(49,118,181,0) 75%);}

  .brand{position:absolute;text-align:center;font-weight:600;letter-spacing:.08em;text-transform:uppercase;line-height:1.15}
  .brand__mark{display:block;margin:0 auto 10px;width:56px;height:56px;border-radius:50%}
  .brand__name{display:block;font-size:30px}
  .brand__sub{display:block;font-size:11px;letter-spacing:.12em}

  .card--front .brand{left:60px;top:90px;width:300px;color:var(--white)}
  .card--front .brand__mark{background:var(--white)}
  .services{position:absolute;left:30px;width:358px;top:270px;text-align:center}
  .services__lead{font-weight:700;font-size:14px;letter-spacing:.01em}
  .services__list{font-size:14.5px;margin-top:3px}
  .since{position:absolute;left:561px;top:169px;transform:translate(-50%,-50%) rotate(-90deg);
    white-space:nowrap;font-size:14px;letter-spacing:.02em}

  .card--back .brand{left:30px;top:24px;width:220px;color:var(--royal-light);text-align:left}
  .card--back .brand__mark{background:var(--royal-light);margin:0 0 10px 78px}
  .card--back .brand__name{font-size:24px}
  .card--back .brand__sub{font-size:9.5px;color:var(--royal-light)}

  .address{position:absolute;left:41px;top:177px;font-size:14.5px;line-height:20px}
  .contact{position:absolute;left:41px;top:225px;font-size:14.5px;line-height:20px;list-style:none}
  .contact li{display:flex;align-items:center;gap:5px}
  .contact svg{width:14px;height:14px;fill:var(--royal)}
  .license{position:absolute;left:41px;top:290px;font-size:14.5px}

  .person{position:absolute;right:37px;top:82px;text-align:right}
  .person__name{color:var(--royal);font-weight:700;font-size:18px;letter-spacing:.02em}
  .person__role{font-size:14.5px;margin-top:1px}
  .person-tab{position:absolute;right:0;top:83px;width:14px;height:40px;background:var(--royal)}

  .badges{position:absolute;left:352px;top:238px;display:flex;align-items:center;gap:10px}
  .badge{background:#c9ccd3}
  .badge--wide{width:92px;height:28px;background:#d8d8d8;border:2px solid #b3262b}
  .badge--tall{width:34px;height:52px;background:var(--royal)}
  .badge--hex{width:54px;height:44px;background:#2e2e2e;clip-path:polygon(25% 0,75% 0,100% 50%,75% 100%,25% 100%,0 50%)}

  .footer-bar{position:absolute;left:0;bottom:0;width:312px;height:13px;background:var(--charcoal)}
  .footer-band{position:absolute;right:0;bottom:0;width:290px;height:29px;background:var(--royal);
    clip-path:polygon(28px 0,100% 0,100% 100%,0 100%)}
  .website{position:absolute;right:37px;bottom:7px;color:var(--white);font-size:14.5px}
</style>
</head>
<body>

<section class="card card--front">
  <div class="state-map" role="img" aria-label="Faint map of the state of Florida"></div>
  <div class="brand">
    <span class="brand__mark"></span>
    <span class="brand__name">Summitcrest</span>
    <span class="brand__sub">Roofing &amp; Gutters Inc.</span>
  </div>
  <div class="services">
    <p class="services__lead">RESIDENTIAL &amp; COMMERCIAL</p>
    <p class="services__list">Fully Insured • Insurance Claims • Free Estimates</p>
  </div>
  <p class="since">Serving Central Florida Since 1992</p>
</section>

<section class="card card--back">
  <div class="brand">
    <span class="brand__mark"></span>
    <span class="brand__name">Summitcrest</span>
    <span class="brand__sub">Roofing &amp; Gutters Inc.</span>
  </div>

  <p class="address">4276 Pellman Crossing Rd<br>Orlando, Fl 32825</p>
  <ul class="contact">
    <li><svg viewBox="0 0 14 14"><path d="M4 0h6a1 1 0 0 1 1 1v12a1 1 0 0 1-1 1H4a1 1 0 0 1-1-1V1a1 1 0 0 1 1-1zm.5 2v8.5h5V2zM7 11.3a.8.8 0 1 0 0 1.6.8.8 0 0 0 0-1.6z"/></svg>(407) 583-2716</li>
    <li><svg viewBox="0 0 14 14"><path d="M3 0.5l2.2 2.8-1.2 1.6c.8 1.9 2.3 3.4 4.2 4.2l1.6-1.2 2.8 2.2-1.1 2.6C6 12.4 1.6 8 .4 1.6z"/></svg>(407) 583-2716</li>
    <li><svg viewBox="0 0 14 14"><path d="M1 3h12v8H1zm1.2 1 4.8 3.6L11.8 4zM2 5.2V10h10V5.2L7 8.9z"/></svg>daniel@SummitcrestShinglesFl.com</li>
  </ul>
  <p class="license">License # CCC4872196</p>

  <div class="person">
    <p class="person__name">DANIEL WHITFIELD</p>
    <p class="person__role">Project Manager</p>
  </div>
  <div class="person-tab"></div>

  <div class="badges" aria-label="Accreditations">
    <div class="badge badge--wide"></div>
    <div class="badge badge--tall"></div>
    <div class="badge badge--hex"></div>
  </div>

  <div class="footer-bar"></div>
  <div class="footer-band"></div>
  <p class="website">www.SummitcrestShinglesFl.com</p>
</section>

</body>
</html>
```